Business card for massage therapy company called Brook Fern Wellness

Need business card for massage therapy company called Brook Fern Wellness. Would like my logo on the front and the back of the card I have 3 options of logos and you can play with what looks better.

Would like this information displayed on the back of the card:

Marcus Ellery
Licensed Massage Therapist
321-555-0147
brookfern-example.com
brookfern_rest_

```html
<!DOCTYPE html>
<html lang="en">
<head>
<meta charset="utf-8">
<title>Brook Fern Wellness – Business Card</title>
<link rel="stylesheet" href="https://fonts.googleapis.com/css2?family=Poppins:wght@400;500&display=swap">
<style>
  :root {
    --backdrop: #cccbb6;
    --paper: #ffffff;
    --sage: #9c9a7b;
    --sage-deep: #8d8d6f;
    --ink: #6f705b;
    --ink-soft: #9a9a7c;
    --mist: #ecece5;
  }
  * { margin: 0; padding: 0; box-sizing: border-box; }
  html, body {
    width: 815px; height: 1200px; overflow: hidden;
    background: var(--backdrop);
    font-family: "Poppins", sans-serif;
  }
  .canvas { position: relative; width: 815px; height: 1200px; }
  .card {
    position: absolute; left: 82px; width: 651px; height: 434px;
    background: var(--paper); overflow: hidden;
  }
  .card--front { top: 109px; }
  .card--back { top: 646px; }
  .card__art { position: absolute; inset: 0; width: 100%; height: 100%; }

  .brand {
    position: absolute; left: 0; right: 0; top: 178px;
    text-align: center; color: var(--paper); font-weight: 400;
  }
  .brand__name { font-size: 42px; letter-spacing: 1px; line-height: 1.1; }
  .brand__tag { font-size: 17px; letter-spacing: 8px; margin-top: 6px; }

  .spa-scene {
    position: absolute; left: 281px; top: 160px; width: 360px; height: 265px;
    background: radial-gradient(ellipse at center, var(--mist) 0%, rgba(236,236,229,0.4) 70%, rgba(236,236,229,0) 100%);
    border-radius: 40px;
  }

  .contact { position: absolute; left: 69px; top: 174px; }
  .contact__name {
    font-size: 36px; font-weight: 500; letter-spacing: 3px; color: var(--ink);
    line-height: 1;
  }
  .contact__rule { width: 272px; height: 3px; background: var(--sage); margin-top: 9px; }
  .contact__role {
    font-size: 13px; font-weight: 500; letter-spacing: 1.6px; color: var(--ink-soft);
    margin-top: 8px;
  }
  .contact__list { list-style: none; margin-top: 6px; }
  .contact__item {
    display: flex; align-items: center; gap: 12px;
    font-size: 14.5px; letter-spacing: 2.2px; color: var(--ink-soft);
    height: 26.5px;
  }
  .contact__icon { width: 17px; height: 17px; flex: none; }
</style>
</head>
<body>
<main class="canvas">

  <section class="card card--front" aria-label="Card front">
    <svg class="card__art" viewBox="0 0 1262 841" preserveAspectRatio="none" aria-hidden="true">
      <path fill="var(--sage)" d="M180,0 L1262,0 L1262,420 C1180,460 1100,540 1040,600 C950,650 850,690 700,715 C560,745 400,745 300,750 C200,745 120,700 0,680 L0,335 C100,320 160,240 230,190 C300,120 420,110 520,60 C560,35 580,20 530,17 Z"/>
      <path fill="var(--sage)" d="M470,841 C560,815 700,790 900,788 C1000,792 1050,805 1090,780 C1150,740 1220,742 1262,745 L1262,841 Z"/>
      <path fill="var(--sage)" d="M0,60 C10,100 12,140 8,200 L0,841 L18,841 C30,800 32,760 28,740 L0,740 Z"/>
      <path fill="none" stroke="var(--sage-deep)" stroke-width="6" d="M30,750 C200,760 400,770 600,770 C800,760 950,745 1060,700"/>
      <path fill="none" stroke="var(--sage-deep)" stroke-width="6" d="M1262,640 C1220,660 1160,690 1120,720"/>
      <path fill="none" stroke="var(--sage-deep)" stroke-width="5" d="M950,25 C1010,30 1050,80 1100,90 C1150,95 1220,95 1262,95"/>
    </svg>
    <div class="brand">
      <div class="brand__name">Brook Fern</div>
      <div class="brand__tag">WELLNESS</div>
    </div>
  </section>

  <section class="card card--back" aria-label="Card back">
    <svg class="card__art" viewBox="0 0 1262 841" preserveAspectRatio="none" aria-hidden="true">
      <path fill="var(--sage)" d="M22,22 C200,5 400,5 480,15 C540,30 580,55 640,68 C750,70 850,88 960,70 C1050,55 1100,40 1140,12 L1180,0 L1262,0 L1262,310 C1200,300 1150,282 1100,275 C1000,275 920,258 860,230 C780,198 760,180 730,160 C680,118 640,110 500,110 C400,112 300,140 220,135 C195,112 150,108 100,94 C60,80 32,50 22,22 Z"/>
      <path fill="none" stroke="var(--sage)" stroke-width="5" d="M25,95 C70,85 100,90 130,105 C170,125 200,120 220,140"/>
      <path fill="none" stroke="var(--sage)" stroke-width="5" d="M900,255 C960,275 1040,280 1100,295 C1180,305 1220,330 1262,340"/>
      <path fill="none" stroke="var(--sage)" stroke-width="5" d="M580,841 C650,820 700,800 740,790 C800,770 860,755 900,755 C960,762 1000,775 1040,760 C1120,750 1200,730 1262,700"/>
    </svg>
    <div class="spa-scene" role="img" aria-label="Line illustration of rolled towels, candles and stacked stones"></div>
    <div class="contact">
      <h1 class="contact__name">MARCUS ELLERY</h1>
      <div class="contact__rule"></div>
      <p class="contact__role">LICENSED MASSAGE THERAPIST</p>
      <ul class="contact__list">
        <li class="contact__item">
          <svg class="contact__icon" viewBox="0 0 24 24" aria-hidden="true"><path fill="var(--ink)" d="M6.6 10.8a15.1 15.1 0 0 0 6.6 6.6l2.2-2.2c.3-.3.7-.4 1-.2 1.1.4 2.3.6 3.6.6.6 0 1 .4 1 1V20c0 .6-.4 1-1 1A17 17 0 0 1 3 4c0-.6.4-1 1-1h3.5c.6 0 1 .4 1 1 0 1.3.2 2.5.6 3.6.1.3 0 .7-.2 1z"/></svg>
          <span>321-555-0147</span>
        </li>
        <li class="contact__item">
          <svg class="contact__icon" viewBox="0 0 24 24" aria-hidden="true" fill="none" stroke="var(--ink)" stroke-width="1.6"><circle cx="12" cy="12" r="10"/><ellipse cx="12" cy="12" rx="4.5" ry="10"/><path d="M2 12h20M4 7h16M4 17h16"/></svg>
          <span>BROOKFERN-EXAMPLE.COM</span>
        </li>
        <li class="contact__item">
          <svg class="contact__icon" viewBox="0 0 24 24" aria-hidden="true"><rect x="3" y="3" width="18" height="18" rx="3" fill="none" stroke="var(--ink)" stroke-width="2"/></svg>
          <span>BROOKFERN_REST_</span>
        </li>
      </ul>
    </div>
  </section>

</main>
</body>
</html>
```